Business Card *

A business card design
Use the logo uploaded in the brief page.
You may use placeholders in your design layouts.
I will provide the actual business card details to the winning designer.

Logo
Place for contact info (name, title, phone, email, etc)

Requirements
Must have
• Logo

```html
<!DOCTYPE html>
<html lang="en">
<head>
<meta charset="utf-8">
<title>Brackenfold Business Card</title>
<link href="https://fonts.googleapis.com/css2?family=Roboto:wght@300;400;500;700&display=swap" rel="stylesheet">
<style>
  :root {
    --backdrop: #1c1f26;
    --card-dark: #1e1e1e;
    --card-dark-tone: #2a2a2a;
    --card-light: #ffffff;
    --green: #3fb23f;
    --green-light: #7cc242;
    --grey: #8a8a8a;
    --icon-grey: #b5b5b5;
    --text: #3a3a3a;
  }
  * { margin: 0; padding: 0; box-sizing: border-box; }
  html, body { width: 1200px; height: 1200px; overflow: hidden; }
  body {
    background: var(--backdrop);
    font-family: "Roboto", Arial, sans-serif;
    display: flex;
    flex-direction: column;
    align-items: center;
    justify-content: center;
    gap: 80px;
  }
  .card {
    width: 760px;
    height: 440px;
    border-radius: 34px 4px 34px 4px;
    position: relative;
    overflow: hidden;
  }
  .card-back { background: var(--card-dark); }
  .card-back .pattern {
    position: absolute;
    inset: 0;
    background: radial-gradient(circle at 50% 40%, var(--card-dark-tone), var(--card-dark));
  }
  .card-front { background: var(--card-light); }

  .brand {
    position: absolute;
    left: 60px;
    top: 160px;
    display: flex;
    align-items: center;
    gap: 12px;
  }
  .brand-mark {
    width: 30px; height: 30px;
    border-radius: 50%;
    background: var(--green);
    flex: none;
  }
  .brand-name {
    font-size: 34px;
    font-weight: 700;
    color: var(--grey);
    letter-spacing: 0.5px;
    line-height: 1;
  }

  .social {
    position: absolute;
    left: 70px;
    top: 272px;
    display: flex;
    gap: 14px;
  }
  .social span {
    width: 32px; height: 32px;
    border-radius: 6px;
    background: var(--icon-grey);
  }

  .person {
    position: absolute;
    right: 50px;
    top: 80px;
    text-align: right;
  }
  .person-name {
    font-size: 40px;
    font-weight: 400;
    color: var(--green);
    letter-spacing: 0.5px;
    line-height: 1.1;
  }
  .person-name .surname { color: var(--green-light); }
  .person-title {
    font-size: 24px;
    font-weight: 300;
    color: var(--text);
    margin-top: 2px;
  }

  .divider {
    position: absolute;
    left: 384px;
    top: 232px;
    width: 2px;
    height: 110px;
    background: linear-gradient(var(--green), rgba(63,178,63,0));
  }

  .contacts {
    position: absolute;
    left: 406px;
    top: 238px;
    list-style: none;
  }
  .contacts li {
    display: flex;
    align-items: center;
    gap: 14px;
    font-size: 18px;
    color: var(--text);
    height: 26px;
  }
  .contacts svg { width: 18px; height: 18px; flex: none; }

  .address {
    position: absolute;
    left: 60px;
    bottom: 36px;
    font-size: 16px;
    color: var(--text);
  }
  .band {
    position: absolute;
    left: 0; right: 0; bottom: 0;
    height: 14px;
    background: var(--green);
  }
</style>
</head>
<body>
  <section class="card card-back">
    <div class="pattern" role="img" aria-label="Repeating pattern of the company emblem in dark tones"></div>
  </section>

  <section class="card card-front">
    <div class="brand">
      <span class="brand-mark"></span>
      <span class="brand-name">BRACKENFOLD</span>
    </div>

    <div class="social" aria-label="Social media links">
      <span></span><span></span><span></span><span></span>
    </div>

    <div class="person">
      <h1 class="person-name">MARCUS <span class="surname">DELANE</span></h1>
      <p class="person-title">Executive Director</p>
    </div>

    <div class="divider"></div>

    <ul class="contacts">
      <li>
        <svg viewBox="0 0 18 18"><circle cx="9" cy="9" r="9" fill="#3fb23f"/><rect x="4.5" y="6" width="9" height="6.5" fill="none" stroke="#fff" stroke-width="1.3"/><path d="M4.5 6 L9 10 L13.5 6" fill="none" stroke="#fff" stroke-width="1.3"/></svg>
        info@brackenfold.com.au
      </li>
      <li>
        <svg viewBox="0 0 18 18"><circle cx="9" cy="9" r="9" fill="#3fb23f"/><rect x="6.2" y="4" width="5.6" height="10" rx="1" fill="none" stroke="#fff" stroke-width="1.3"/><circle cx="9" cy="12" r="0.7" fill="#fff"/></svg>
        +61255501234
      </li>
      <li>
        <svg viewBox="0 0 18 18"><circle cx="9" cy="9" r="9" fill="#3fb23f"/><path d="M6 4.5 L8 6.8 L7 8.2 Q8 10.4 9.8 11 L11.2 10 L13.5 12 L12.3 13.6 Q8 13.5 4.5 6 Z" fill="#fff"/></svg>
        +61255501234
      </li>
      <li>
        <svg viewBox="0 0 18 18"><circle cx="9" cy="9" r="9" fill="#3fb23f"/><circle cx="9" cy="9" r="4.6" fill="none" stroke="#fff" stroke-width="1.2"/><ellipse cx="9" cy="9" rx="2" ry="4.6" fill="none" stroke="#fff" stroke-width="1"/><line x1="4.4" y1="9" x2="13.6" y2="9" stroke="#fff" stroke-width="1"/></svg>
        www.brackenfold.com.au
      </li>
    </ul>

    <p class="address">Address: Suite 9, 14 Harlow Lane, Belmont ACT 2900&nbsp;&nbsp;ABN: 47 215 330 908</p>
    <div class="band"></div>
  </section>
</body>
</html>
```